Moms Beyond Gnatflies

My company name is Moms beyond gnatflies. We do residential and commercial mosquito control. See attached brochure and logo.

Target Market(s)

My target market is upper middle class families in the midwestern part of the US.

Requirements
Must have
• Form to collect customer information

```html
<!DOCTYPE html>
<html lang="en">
<head>
<meta charset="utf-8">
<title>Moms Beyond Gnatflies – Mosquito Control</title>
<link rel="stylesheet" href="https://fonts.googleapis.com/css2?family=Arimo:wght@400;700&family=Nunito:wght@900&family=Oswald:wght@400;500;600&family=Montserrat:wght@800&family=Anton&display=swap">
<style>
:root{
  --green-dark:#0c5f2a;
  --green-mid:#1a7a34;
  --green-bright:#2fae2f;
  --form-green:#0f4d1c;
  --yellow:#fff200;
  --yellow-soft:#f4e23a;
  --arrow-yellow:#e3d41d;
  --text-grey:#4a4a4a;
  --heading-grey:#6b6b6b;
  --ink:#111;
  --sky-top:#ffffff;
  --sky-mid:#cfe2f0;
  --sky-low:#e9f1f7;
}
*{box-sizing:border-box;margin:0;padding:0}
html,body{width:1200px;height:900px;overflow:hidden}
body{
  position:relative;
  font-family:"Arimo",Arial,sans-serif;
  background:linear-gradient(180deg,var(--sky-top) 0,var(--sky-top) 170px,var(--sky-mid) 330px,#dbe9f3 520px,var(--sky-low) 700px,#fff 800px);
}
.abs{position:absolute}

/* brand */
.brand{left:160px;top:40px;display:flex;align-items:center;gap:12px}
.brand-dot{width:22px;height:22px;border-radius:50%;background:var(--green-dark);flex:none}
.brand-name{font-family:"Oswald",sans-serif;font-weight:600;font-size:34px;line-height:1.02;color:var(--green-dark);width:220px}

/* top promo */
.promo-band{left:490px;top:14px}
.promo-title{left:500px;top:20px;width:560px;font-family:"Nunito",sans-serif;font-weight:900;font-size:29px;line-height:30px;color:var(--green-dark);text-shadow:1px 1px 0 rgba(0,0,0,.25)}
.promo-call{left:497px;top:89px;font-family:"Oswald",sans-serif;font-weight:500;font-size:33px;color:#333;white-space:nowrap;letter-spacing:-.5px}
.promo-call .paren{color:var(--green-bright);font-weight:400}
.promo-call .digits{color:var(--green-dark)}
.promo-call small{font-weight:400;font-size:19px;color:#555;letter-spacing:0}

/* eco */
.eco-badge{left:614px;top:170px}
.eco-line{font-family:"Oswald",sans-serif;font-weight:400;color:var(--heading-grey);white-space:nowrap}
.eco-line.one{left:746px;top:172px;font-size:24.5px}
.eco-line.two{left:766px;top:202px;font-size:23px}
.eco-line strong{color:var(--green-dark);font-weight:600}

/* collage */
.photo.kids{left:718px;top:238px;width:104px;height:164px;background:linear-gradient(160deg,#5d8a3a,#a9b98a 60%,#7a6a4e)}
.photo.cafe{left:828px;top:238px;width:220px;height:92px;background:linear-gradient(120deg,#b98a64,#d9c39a 50%,#8aa66a)}
.photo.sky-gap{left:826px;top:334px;width:107px;height:68px;background:#8ec7ea}
.photo.pool{left:718px;top:406px;width:214px;height:129px;background:linear-gradient(180deg,#6f7a4a,#c9c1a4 45%,#4fb3d6 70%,#2d8fbd)}
.photo.office{left:937px;top:334px;width:111px;height:201px;background:linear-gradient(180deg,#5a8a3c,#8a7460 50%,#6d6e72)}

/* info sections */
.q-arrow{width:58px;height:30px}
.q-head{font-family:"Montserrat",sans-serif;font-weight:800;color:var(--green-dark);font-size:34px;white-space:nowrap;line-height:1}
.q-head span{font-family:"Oswald",sans-serif;font-weight:500;font-size:18px;letter-spacing:-.3px;margin-left:-6px}
.q-text{font-size:14px;line-height:19px;color:var(--text-grey)}

.highlight{left:140px;top:574px;width:556px;height:28px;background:var(--yellow);transform:skewX(-4deg) rotate(-.4deg)}
.highlight-text{left:148px;top:578px;font-family:"Oswald",sans-serif;font-weight:500;font-size:17.6px;color:var(--green-dark);white-space:nowrap;letter-spacing:-.3px}

/* bee bubble */
.bee-bubble{left:143px;top:630px;width:195px;height:160px;border-radius:50%;background:var(--yellow-soft)}
.bee-text{left:128px;top:646px;width:225px;text-align:center;font-family:"Anton",sans-serif;color:#111;transform:rotate(-10deg);line-height:1;white-space:nowrap}
.bee-text .s1{font-size:19px;display:block}
.bee-text .s3{font-size:26px;display:block;margin-top:2px}

.pitch{left:375px;top:620px;width:320px;font-size:17px;line-height:22.5px;color:var(--ink)}
.pitch strong{display:block;margin-top:25px;font-weight:700;font-size:16.5px;line-height:24px}

/* form */
.form-back{left:694px;top:544px}
.form-title{left:720px;top:547px;font-family:"Oswald",sans-serif;font-weight:500;font-size:19.5px;color:var(--form-green);letter-spacing:-.4px}
.request-form{left:718px;top:570px;width:331px;height:252px;background:var(--form-green);border-radius:10px;color:#fff}
.field{position:absolute;left:15px;display:flex;align-items:center}
.field label{width:49px;font-size:14px}
.field input{width:247px;height:28px;border:1px solid #cfcfcf;background:#fff}
.field.name{top:22px}.field.email{top:58px}.field.phone{top:96px}
.ask{position:absolute;left:18px;top:137px;font-size:14px;color:#e6efe6}
.choices{position:absolute;left:16px;top:164px;display:flex;gap:18px;font-size:14px}
.choices label{display:flex;align-items:center;gap:8px}
.choices input{appearance:none;width:14px;height:14px;background:#ddd;border:1px solid #aaa}
.submit{position:absolute;left:192px;top:183px;width:128px;height:50px;border:1px solid #c9b21c;border-radius:4px;background:linear-gradient(180deg,#fff59a,#f2dc3a 50%,#d8b91c);font-family:"Arimo",sans-serif;font-weight:700;font-size:20px;color:#1d5a1d;letter-spacing:.5px}

.copyright{left:146px;top:861px;font-size:12px;color:var(--green-mid)}
</style>
</head>
<body>

<div class="abs brand">
  <span class="brand-dot"></span>
  <span class="brand-name">Moms Beyond Gnatflies</span>
</div>

<svg class="abs promo-band" width="580" height="80" viewBox="0 0 580 80" aria-hidden="true">
  <polygon points="4,4 560,14 566,34 470,46 440,64 12,70" fill="var(--yellow)"/>
</svg>
<h1 class="abs promo-title">Rid your outside areas of pesky and dangerous bugs the safe way!</h1>
<p class="abs promo-call">CALL <span class="paren">(</span><span class="paren">555</span><span class="paren">)</span> <span class="digits">014-2760</span> <small>to schedule an evaluation.</small></p>

<div class="abs photo kids" role="img" aria-label="Two children walking hand in hand along a garden path"></div>
<div class="abs photo cafe" role="img" aria-label="Friends laughing together at an outdoor café table"></div>
<div class="abs photo sky-gap"></div>
<div class="abs photo pool" role="img" aria-label="Hotel swimming pool with white umbrellas and lounge chairs"></div>
<div class="abs photo office" role="img" aria-label="Business people talking in an outdoor courtyard"></div>

<svg class="abs eco-badge" width="140" height="140" viewBox="0 0 140 140" aria-hidden="true">
  <circle cx="69" cy="67" r="64" fill="#fff" stroke="var(--green-mid)" stroke-width="5"/>
  <circle cx="69" cy="67" r="46" fill="none" stroke="var(--green-mid)" stroke-width="3"/>
</svg>
<p class="abs eco-line one">environmentally-friendly</p>
<p class="abs eco-line two"><strong>EPA-APPROVED</strong> treatment</p>

<svg class="abs q-arrow" style="left:150px;top:210px" viewBox="0 0 58 30" aria-hidden="true"><polygon points="0,6 36,6 36,0 58,12 36,28 36,20 0,20" fill="var(--arrow-yellow)" transform="rotate(8 29 15)"/></svg>
<h2 class="abs q-head" style="left:205px;top:207px">WHAT <span>IS MOMS BEYOND GNATFLIES?</span></h2>
<p class="abs q-text" style="left:155px;top:248px;width:420px">Moms Beyond Gnatflies is the only scheduled spraying service devoted exclusively to protecting your outdoor area against mosquitoes and other pests all season long!</p>

<svg class="abs q-arrow" style="left:145px;top:333px" viewBox="0 0 58 30" aria-hidden="true"><polygon points="0,6 36,6 36,0 58,12 36,28 36,20 0,20" fill="var(--arrow-yellow)" transform="rotate(8 29 15)"/></svg>
<h2 class="abs q-head" style="left:205px;top:330px">WHY <span>USE MOMS BEYOND GNATFLIES?</span></h2>
<p class="abs q-text" style="left:155px;top:374px;width:530px">West Nile Virus is a real threat! Illinois is one of the states with the most confirmed human cases.&nbsp; M.B.G! will protect your business against West Nile and eliminate or reduce the dangers of Encephalitis and allergic reactions caused by insect bites.</p>

<svg class="abs q-arrow" style="left:147px;top:460px" viewBox="0 0 58 30" aria-hidden="true"><polygon points="0,6 36,6 36,0 58,12 36,28 36,20 0,20" fill="var(--arrow-yellow)" transform="rotate(8 29 15)"/></svg>
<h2 class="abs q-head" style="left:205px;top:457px">WHERE <span>CAN I SPRAY MOMS BEYOND GNATFLIES?</span></h2>
<p class="abs q-text" style="left:155px;top:498px;width:520px">Anywhere outside. M.B.G! offers excellent service for public pools, outdoor cafés and beer gardens, baseball fields, courtyards, public places such as fountains or town squares, and office gathering areas.</p>

<div class="abs highlight"></div>
<p class="abs highlight-text">Once applied, M.B.G! is a long acting product that remains effective for weeks.</p>

<div class="abs bee-bubble"></div>
<p class="abs bee-text">
  <span class="s1">Now offering<br>“BEE FRIENDLY”<br>bee deterrent!</span>
  <span class="s3">great for outside<br>eating areas!</span>
</p>

<p class="abs pitch">Keep your customers and employees enjoying the summer weather without the inconvenience of mosquitoes, ticks, lice and other insects.
<strong>Call (555) 014-2760 to schedule an evaluation appointment or feel out the form to the right.</strong></p>

<svg class="abs form-back" width="360" height="292" viewBox="0 0 360 292" aria-hidden="true">
  <polygon points="0,4 352,10 356,284 30,290" fill="var(--yellow)"/>
</svg>
<h3 class="abs form-title">REQUEST INFORMATION</h3>
<form class="abs request-form">
  <div class="field name"><label for="f-name">Name</label><input id="f-name" type="text"></div>
  <div class="field email"><label for="f-email">Email</label><input id="f-email" type="email"></div>
  <div class="field phone"><label for="f-phone">Phone</label><input id="f-phone" type="tel"></div>
  <p class="ask">I would like to schedule an evaluation?</p>
  <div class="choices">
    <label><input type="checkbox"> yes</label>
    <label><input type="checkbox"> not yet</label>
  </div>
  <button class="submit" type="button">SUBMIT</button>
</form>

<p class="abs copyright">Copyright 2010 Mom's Beyond Gnatflies! All Rights Reserved</p>

</body>
</html>
```